lighting products eshop web site

We need a brand new ecommerce website (only psd files for the layout) , that will sell professional lighting products in Greek territory.
Please check the sister site www.lampiroxa.gr to get an idea of the products, they will be similar, actually like the products under the menu category "ΕΠΑΓΓΕΛΜΑΤΙΚΑ".
We would like the same philosophy as far as concern the menu structure, namely the menu categories/subcategories shall be actually the products
categories/subcategories, however the menu items shall be presented in a different, more sophisticated way. As far as concern the website layout, we need a minimal, elegant
and contemporary approach that will highlight the products in a perfect manner. We prefer the white color as the main website (background) color and discrete use of brand logo colors.
That is the main idea, awaiting your personal proposal according to the aforementioned requirements
Technically speaking we use bootstrap framework in terms of design meaning 12cols with max width 1170px.
The website will be a joomla - virtuemart website

For images please use some from lampiroxa.gr
For text use any text - just to show me the space.

Industry/Entity Type

It Professional

Number of Pages Required

3 page

Font styles to use
Sans Serif

Colors
00a990
ec1f27

Requirements
Must have
• I need 4 psd pages for the website
• 1. Start page
• 2. Category page
• 3. Product details page
• 4. blog page
Nice to have
• leave designer to choose the best

```html
<!DOCTYPE html>
<html lang="en">
<head>
<meta charset="utf-8">
<title>Lampiroxa – Category</title>
<link href="https://fonts.googleapis.com/css2?family=Montserrat:wght@300;400;600;700&family=Open+Sans:ital,wght@0,400;0,600;1,400&family=Oswald:wght@500&display=swap" rel="stylesheet">
<style>
:root{
  --red:#ec1f27;
  --green:#00a990;
  --ink:#222;
  --muted:#777;
  --line:#e2e2e2;
  --soft:#f4f4f4;
  --footer:#1f1f1f;
  --footer-bottom:#2b2b2b;
  --footer-text:#9a9a9a;
}
*{box-sizing:border-box;margin:0;padding:0}
html,body{width:1200px;height:2233px;overflow:hidden}
body{position:relative;background:#fff;font-family:"Open Sans",Arial,sans-serif;color:var(--ink)}
.abs{position:absolute}
.topbar{left:0;top:0;width:1200px;height:33px;background:var(--red);color:#fff;font-size:11px;line-height:33px}
.topbar .addr{left:144px}
.topbar .call{right:144px}
.search{left:144px;top:57px;width:267px;height:29px;border:1px solid #ccc;border-radius:2px;font-size:11px}
.search .all{position:absolute;left:0;top:0;width:51px;height:27px;border-right:1px solid #ccc;line-height:27px;padding-left:12px;color:#333}
.search .ph{position:absolute;left:62px;top:0;line-height:27px;color:#aaa;font-size:11px}
.search svg{position:absolute;right:10px;top:7px}
.hlinks{top:64px;font-family:Montserrat,sans-serif;font-size:11px;color:#444}
.cart-badge{left:995px;top:58px;width:14px;height:14px;border-radius:50%;background:var(--red);color:#fff;font-size:8px;text-align:center;line-height:14px}
.logo{left:0;width:1200px;top:137px;text-align:center;font-family:Montserrat,sans-serif;font-weight:300;font-size:50px;letter-spacing:10px;color:var(--red)}
.nav{left:0;top:231px;width:1200px;height:48px;border-top:1px solid var(--line);border-bottom:1px solid var(--line)}
.nav span{position:absolute;top:15px;font-family:Montserrat,sans-serif;font-weight:700;font-size:14px;letter-spacing:2px;color:#111}
.nav span.active{color:var(--green)}
.hero{left:0;top:279px;width:1200px;height:317px;background:linear-gradient(90deg,#8fa9c4 0%,#7b9ec4 40%,#7c9dc5 100%)}
.hero h1{position:absolute;left:521px;top:68px;font-family:Montserrat,sans-serif;font-weight:700;font-size:37px;line-height:52px;letter-spacing:6px;color:#fff}
.crumbs{left:0;top:596px;width:1200px;height:47px;background:var(--soft)}
.crumbs p{position:absolute;right:144px;top:16px;font-size:10px;color:#777}
.crumbs em{font-style:normal;color:var(--green)}
.side-title{font-family:Montserrat,sans-serif;font-weight:600;font-size:12px;letter-spacing:4px;color:#111}
.side-rule{height:2px;background:var(--red)}
.side-list{left:155px;top:740px;list-style:none;font-family:Montserrat,sans-serif;font-size:14px;color:#555}
.side-list li{height:19.7px;line-height:19.7px;position:relative;padding-left:20px}
.side-list li::before{content:"";position:absolute;left:0;top:7px;width:6px;height:6px;border:1px solid #bbb}
.side-list li.on{color:var(--red)}
.side-list li.on::before{background:#bbb}
.side-cat{left:144px;font-family:Montserrat,sans-serif;font-size:13px;color:#222}
.toolbar{left:380px;top:669px;width:676px;height:24px;border-bottom:1px solid var(--line);font-size:11px;color:#444}
.card{width:209px;border:1px solid #d8d8d8;background:#fff}
.photo{position:absolute;left:16px;right:16px;top:20px;bottom:20px;background:radial-gradient(circle,#d7d7d7 0%,#f3f3f3 70%,#fff 100%)}
.pinfo{width:209px;text-align:center}
.pinfo h3{font-family:Montserrat,sans-serif;font-weight:700;font-size:14px;letter-spacing:3px;color:#111}
.pinfo p{font-family:Montserrat,sans-serif;font-size:12px;color:#888;margin-top:10px}
.price{font-family:Montserrat,sans-serif;font-size:11px;margin-top:5px;color:#555}
.price b{color:#111;margin-left:8px}
.price i{color:var(--red);margin-left:8px;font-weight:600}
.featured{box-shadow:4px 6px 10px rgba(0,0,0,.18)}
.loading{left:0;width:1200px;top:1558px;text-align:center;font-family:Montserrat,sans-serif;font-size:12px;letter-spacing:4px;color:#555}
.lower-band{left:0;top:1300px;width:1200px;height:555px;background:#fbfbfb}
.feature{top:1645px;height:152px;width:296px;border:1px dashed #d4d4d4;text-align:center;background:#fff}
.feature svg{margin-top:26px}
.feature h4{font-family:Montserrat,sans-serif;font-weight:400;font-size:11px;color:#333;margin-top:14px}
.feature p{font-style:italic;font-size:10px;color:#555;margin-top:6px}
.footer{left:0;top:1855px;width:1200px;height:326px;background:var(--footer)}
.fcol{top:36px}
.fcol h5{font-family:Oswald,sans-serif;font-weight:500;font-size:14px;color:#fff;border-left:2px solid var(--green);padding-left:10px;text-transform:uppercase;letter-spacing:-.2px}
.fcol ul{list-style:none;margin-top:43px;font-size:11px;color:var(--footer-text)}
.fcol li{height:28px;padding-left:14px;position:relative}
.fcol.links li::before{content:"";position:absolute;left:0;top:6px;width:4px;height:4px;border-radius:50%;background:#888}
.fcol.about li{padding-left:36px}
.fcol.about svg{position:absolute;left:12px;top:1px}
.pay{top:206px;width:28px;height:16px;background:#e8e8e8;border-radius:2px}
.fbottom{left:0;top:2181px;width:1200px;height:52px;background:var(--footer-bottom)}
.fbottom p{position:absolute;left:152px;top:18px;font-size:11px;color:#aaa}
.social{top:21px;width:10px;height:10px;border-radius:50%;background:#8a8a8a}
</style>
</head>
<body>

<div class="abs topbar"><span class="abs addr">18 Kifisias Ave, Marousi 15125</span><span class="abs call">Call us -210-555-0147</span></div>

<div class="abs search"><span class="all">All ▾</span><span class="ph">Search for your categories.......</span>
<svg width="12" height="12" viewBox="0 0 12 12"><circle cx="5" cy="5" r="4" fill="none" stroke="#999" stroke-width="1.2"/><line x1="8" y1="8" x2="11.5" y2="11.5" stroke="#999" stroke-width="1.2"/></svg></div>
<span class="abs hlinks" style="left:850px">HOME</span>
<span class="abs hlinks" style="left:905px">ACCOUNT</span>
<svg class="abs" style="left:980px;top:61px" width="17" height="18" viewBox="0 0 17 18"><path d="M2 5h13l-1 12H3z M5 5V3.5a3.5 3.5 0 0 1 7 0V5" fill="none" stroke="#444" stroke-width="1.3"/></svg>
<span class="abs cart-badge">0</span>
<span class="abs hlinks" style="left:1015px;top:63px;font-size:13px;color:#333">$0.00</span>

<div class="abs logo">LAMPIROXA</div>

<nav class="abs nav">
  <span class="active" style="left:153px">HANGING</span>
  <span style="left:265px">ROOF</span>
  <span style="left:338px">WALL</span>
  <span style="left:411px">FLOOR</span>
  <span style="left:497px">SPOT</span>
  <span style="left:579px">OUTDOOR</span>
  <span style="left:694px">FANS</span>
  <span style="left:782px">PROFESSIONAL</span>
  <span style="left:954px">COMPANY</span>
</nav>

<section class="abs hero" role="img" aria-label="Interior photo: pendant lamp and table lamp over a shelf of potted plants against a blue wall">
  <h1>LOOKING FOR A<br>HOME WITH<br>BEAUTIFUL LIGHTS?</h1>
</section>

<div class="abs crumbs"><p>HOME / <em>CATEGORY</em></p></div>

<!-- sidebar -->
<div class="abs side-title" style="left:144px;top:669px">CATEGORIES</div>
<div class="abs side-rule" style="left:144px;top:690px;width:178px"></div>
<div class="abs side-cat" style="left:144px;top:708px;font-weight:700">PROFESSIONAL &nbsp;&nbsp;-</div>
<ul class="abs side-list">
  <li>DOWNLIGHTS</li><li class="on">SPOT TRACK</li><li>LINEAR</li><li>LAMPS</li><li>LIGHTS</li>
  <li>PROFILE ALUMINIUM</li><li>MOVIES LEDs</li><li>LIGHTS</li><li>PROFILE ALUMINIUM</li><li>MOVIES LEDs</li>
</ul>
<div class="abs side-cat" style="top:961px">OUTDOORS &nbsp;&nbsp;&nbsp;&nbsp;+</div>
<div class="abs side-cat" style="top:997px">FANS &nbsp;&nbsp;&nbsp;&nbsp;&nbsp;&nbsp;&nbsp;&nbsp;&nbsp;&nbsp;&nbsp;&nbsp;+</div>
<div class="abs side-cat" style="top:1036px">WALLS &nbsp;&nbsp;&nbsp;&nbsp;&nbsp;&nbsp;&nbsp;&nbsp;&nbsp;+</div>
<div class="abs side-title" style="left:144px;top:1082px;font-size:9px;letter-spacing:2px">PRICE</div>
<div class="abs side-rule" style="left:144px;top:1101px;width:178px"></div>
<div class="abs" style="left:144px;top:1119px;font-size:11px;color:#333">Price range: $0 - $ 2000</div>
<div class="abs" style="left:144px;top:1156px;width:173px;height:5px;background:#efeae0"></div>
<div class="abs" style="left:150px;top:1156px;width:106px;height:5px;background:var(--green)"></div>
<div class="abs" style="left:144px;top:1152px;width:13px;height:13px;background:var(--red)"></div>
<div class="abs" style="left:250px;top:1152px;width:13px;height:13px;background:var(--red)"></div>

<!-- toolbar -->
<div class="abs toolbar"><span class="abs" style="left:0;top:0">Showing all 6 Results</span><span class="abs" style="right:0;top:0">Sort: Popular &nbsp;I&nbsp; New &nbsp;&nbsp;I&nbsp; Price : Low &nbsp;High</span></div>

<div class="abs lower-band"></div>

<!-- products row 1 -->
<div class="abs card" style="left:380px;top:740px;height:264px"><div class="photo" role="img" aria-label="White track spotlight"></div></div>
<div class="abs pinfo" style="left:380px;top:1024px"><h3>LOREM IPSUM</h3><p>lorem Ipsum is simply</p><div class="price">$ 2,000<b>$ 900</b><i>(40% Off)</i></div></div>

<div class="abs card" style="left:613px;top:740px;height:264px"><div class="photo" role="img" aria-label="Black LED floodlight"></div></div>
<div class="abs pinfo" style="left:613px;top:1024px"><h3>LOREM IPSUM</h3><p>lorem Ipsum is simply</p><div class="price">$ 2,000<b>$ 900</b><i>(40% Off)</i></div></div>

<div class="abs card featured" style="left:852px;top:740px;height:343px">
  <div class="photo" style="bottom:113px" role="img" aria-label="Recessed LED downlight"></div>
  <svg class="abs" style="left:112px;top:236px" width="90" height="14" viewBox="0 0 90 14">
    <path d="M2 4h10v9H2z M4.5 4V2.5a2.5 2.5 0 0 1 5 0V4" fill="none" stroke="#8a1c1c" stroke-width="1.1"/>
    <path d="M39 1l6 3-6 3-6-3z M33 7l6 3 6-3 M33 10l6 3 6-3" fill="none" stroke="#8a1c1c" stroke-width="1.1"/>
    <path d="M74 13l-5-5a3 3 0 0 1 5-4 3 3 0 0 1 5 4z" fill="#8a1c1c"/>
  </svg>
  <div class="pinfo abs" style="left:0;top:272px;width:207px"><h3>LOREM IPSUM</h3><p style="margin-top:8px">lorem Ipsum is simply</p><div class="price">$ 2,000<b>$ 900</b><i>(40% Off)</i></div></div>
</div>

<!-- products row 2 -->
<div class="abs card" style="left:380px;top:1150px;height:265px"><div class="photo" role="img" aria-label="White LED bulb"></div></div>
<div class="abs pinfo" style="left:380px;top:1436px"><h3>LOREM IPSUM</h3><p>lorem Ipsum is simply</p><div class="price">$ 2,000<b>$ 900</b><i>(40% Off)</i></div></div>

<div class="abs card" style="left:613px;top:1150px;height:265px"><div class="photo" role="img" aria-label="Mesh LED power supply"></div></div>
<div class="abs pinfo" style="left:613px;top:1436px"><h3>LOREM IPSUM</h3><p>lorem Ipsum is simply</p><div class="price">$ 2,000<b>$ 900</b><i>(40% Off)</i></div></div>

<div class="abs card" style="left:846px;top:1150px;height:265px"><div class="photo" role="img" aria-label="Aluminium LED profile"></div></div>
<div class="abs pinfo" style="left:846px;top:1433px"><h3>LOREM IPSUM</h3><p>lorem Ipsum is simply</p><div class="price">$ 2,000<b>$ 900</b><i>(40% Off)</i></div></div>

<div class="abs loading">LOADING......</div>

<!-- features -->
<div class="abs feature" style="left:131px">
  <svg width="30" height="30" viewBox="0 0 30 30"><circle cx="15" cy="13" r="9" fill="none" stroke="#777" stroke-width="1.3"/><path d="M9 24h12 M15 22v2" stroke="#777" stroke-width="1.3"/></svg>
  <h4>FREE SHIPPING WORLDWIDE</h4><p>Free shipping worldwide</p></div>
<div class="abs feature" style="left:451px">
  <svg width="30" height="30" viewBox="0 0 30 30"><path d="M6 18v-4a9 9 0 0 1 18 0v4" fill="none" stroke="#777" stroke-width="1.3"/><rect x="4" y="16" width="5" height="8" rx="1" fill="none" stroke="#777" stroke-width="1.3"/><rect x="21" y="16" width="5" height="8" rx="1" fill="none" stroke="#777" stroke-width="1.3"/></svg>
  <h4>24/7 CUSTOMER SERVICE</h4><p>Service Support 24/7</p></div>
<div class="abs feature" style="left:770px">
  <svg width="30" height="30" viewBox="0 0 30 30"><path d="M6 15a9 9 0 0 1 15-6.5 M24 15a9 9 0 0 1-15 6.5" fill="none" stroke="#777" stroke-width="1.3"/><path d="M21 4v5h-5 M9 26v-5h5" fill="none" stroke="#777" stroke-width="1.3"/></svg>
  <h4>MONEY BACK GUARANTEE!100%</h4><p>Money Back – 30 Days</p></div>

<!-- footer -->
<footer class="abs footer">
  <div class="abs fcol about" style="left:152px">
    <h5>About Store</h5>
    <ul>
      <li><svg width="11" height="11" viewBox="0 0 11 11"><path d="M1 5.5L5.5 1 10 5.5V10H1z" fill="#ccc"/></svg>42 Lumen Street, Athens</li>
      <li><svg width="11" height="11" viewBox="0 0 11 11"><path d="M2 1h2l1 3-1.5 1a6 6 0 0 0 2.5 2.5L7 6l3 1v2a1 1 0 0 1-1 1A8 8 0 0 1 1 2a1 1 0 0 1 1-1z" fill="#ccc"/></svg>(210) 555 0199</li>
      <li><svg width="12" height="10" viewBox="0 0 12 10"><rect x=".5" y=".5" width="11" height="9" fill="none" stroke="#ccc"/><path d="M.5 .5L6 5l5.5-4.5" fill="none" stroke="#ccc"/></svg>hello@lampiroxa.gr</li>
    </ul>
  </div>
  <div class="abs pay" style="left:152px"></div>
  <div class="abs pay" style="left:192px"></div>
  <div class="abs pay" style="left:232px"></div>
  <div class="abs pay" style="left:272px"></div>
  <div class="abs pay" style="left:312px"></div>

  <div class="abs fcol links" style="left:411px"><h5>My Account</h5>
    <ul><li>My Account</li><li>Wishlist</li><li>My Cart</li><li>Checkout</li></ul></div>
  <div class="abs fcol links" style="left:670px"><h5>Information</h5>
    <ul><li>About Us</li><li>Careers</li><li>Delivery Inforamtion</li><li>Privacy Policy</li><li>Terms &amp; Condition</li><li>Sale products</li></ul></div>
  <div class="abs fcol links" style="left:929px"><h5>Customer Service</h5>
    <ul><li>Shipping Policy</li><li>Compensation First</li><li>My Account</li><li>Return Policy</li><li>Contact Us</li><li>Shipping Info</li></ul></div>
</footer>

<div class="abs fbottom">
  <p>Copyright © 2016</p>
  <span class="abs social" style="left:946px"></span>
  <span class="abs social" style="left:992px"></span>
  <span class="abs social" style="left:1039px"></span>
  <span class="abs social" style="left:1088px"></span>
  <span class="abs social" style="left:1134px"></span>
</div>

</body>
</html>
```